Morning Harvest Psalm Journal for the Weary Traveler on the Narrow Road

This is not an Eastern meditation method. No images or themes from guru style or Eastern meditations from Hinduism or Buddhism will work. This is a Biblical Christian-based method. Some sort of Divine Light from Heaven may be the look. Some "ancient scroll" for the title to be written in may work.

```html
<!DOCTYPE html>
<html lang="en">
<head>
<meta charset="utf-8">
<title>Morning Harvest — Cover Spread</title>
<link rel="stylesheet" href="https://fonts.googleapis.com/css2?family=Cinzel:wght@400;600&family=Playfair+Display:wght@700&family=Montserrat:wght@500;600&display=swap">
<style>
  :root {
    --page: #ffffff;
    --night: #000000;
    --gold: #d99a3a;
    --gold-deep: #7a4a18;
    --teal: #1c6a80;
    --ink: #ffffff;
    --title-dark: #0b0704;
  }
  * { margin: 0; padding: 0; box-sizing: border-box; }
  html, body { width: 1200px; height: 1199px; overflow: hidden; background: var(--page); }

  .spread {
    position: absolute; left: 62px; top: 220px;
    width: 1074px; height: 766px;
    background: var(--night);
    overflow: hidden;
  }

  /* back cover */
  .back-cover { position: absolute; left: 0; top: 0; width: 496px; height: 766px; }
  .back-art {
    position: absolute; left: 0; top: 0; width: 496px; height: 512px;
    background: linear-gradient(180deg, #b57828 0%, #8a5a1f 40%, #4a3014 70%, #1a1208 88%, var(--night) 100%);
  }
  .back-title {
    position: absolute; left: 0; width: 496px; top: 68px;
    text-align: center;
    font-family: "Cinzel", serif; font-weight: 600;
    font-size: 19px; line-height: 23px; letter-spacing: 0.12em;
    text-transform: uppercase;
    color: var(--title-dark);
  }
  .back-blurb {
    position: absolute; left: 40px; top: 172px; width: 420px;
    font-family: Arial, Helvetica, sans-serif;
    font-size: 9.8px; line-height: 11.3px; color: var(--ink);
  }
  .back-blurb p + p { margin-top: 11px; }
  .back-author {
    position: absolute; left: 0; width: 496px; top: 558px;
    text-align: center;
    font-family: "Cinzel", serif; font-size: 13px; letter-spacing: 0.95em; padding-left: 0.95em;
    text-transform: uppercase;
    color: var(--ink);
  }

  /* spine */
  .spine { position: absolute; left: 496px; top: 0; width: 82px; height: 766px; }
  .spine-art {
    position: absolute; left: 0; top: 120px; width: 82px; height: 420px;
    background: linear-gradient(180deg, rgba(28,106,128,0) 0%, rgba(28,106,128,.35) 25%, rgba(160,105,40,.45) 65%, rgba(0,0,0,0) 100%);
  }
  .spine-text {
    position: absolute; left: 33px; top: 39px;
    writing-mode: vertical-rl;
    font-family: "Cinzel", serif; font-size: 12.5px; letter-spacing: 0.82em;
    text-transform: uppercase;
    color: var(--ink);
    display: flex; align-items: center;
  }
  .spine-dot {
    display: inline-block; width: 8px; height: 8px; border-radius: 50%;
    background: var(--ink); margin: 60px 0 28px;
  }

  /* front cover */
  .front-cover { position: absolute; left: 578px; top: 0; width: 496px; height: 766px; }
  .front-art {
    position: absolute; left: 0; top: 150px; width: 496px; height: 480px;
    background: radial-gradient(ellipse 260px 230px at 50% 52%, #e2a748 0%, #a8702a 35%, #3a4a50 65%, rgba(0,0,0,0) 100%);
  }
  .series {
    position: absolute; left: 0; width: 496px; top: 32px;
    text-align: center;
    font-family: "Montserrat", sans-serif; font-weight: 600;
    font-size: 10.5px; letter-spacing: 1.05em; padding-left: 1.05em;
    text-transform: uppercase;
    color: var(--ink);
  }
  .front-title {
    position: absolute; left: 0; width: 496px; top: 67px;
    text-align: center;
    font-family: "Playfair Display", serif; font-weight: 700;
    font-size: 54px; line-height: 49px;
    color: var(--ink);
  }
  .front-subtitle {
    position: absolute; left: 0; width: 496px; top: 653px;
    text-align: center;
    font-family: "Montserrat", sans-serif; font-weight: 500;
    font-size: 13.5px; line-height: 23px; letter-spacing: 0.42em; padding-left: 0.42em;
    text-transform: uppercase;
    color: var(--ink);
  }
  .front-author {
    position: absolute; left: 0; width: 496px; top: 732px;
    text-align: center;
    font-family: "Cinzel", serif; font-size: 13px; letter-spacing: 0.95em; padding-left: 0.95em;
    text-transform: uppercase;
    color: var(--ink);
  }
</style>
</head>
<body>
  <main class="spread">
    <section class="back-cover">
      <div class="back-art" role="img" aria-label="Illustration of golden heavenly clouds with divine light from above"></div>
      <h2 class="back-title">For the Weary Traveler<br>on the Narrow Road</h2>
      <div class="back-blurb">
        <p>Each morning brings a quiet harvest for the soul that waits upon the Lord. In these pages you will find thirty days of Psalms, short prayers and honest questions, written for anyone who feels tired on the road that leads to life. This is not a method of emptying the mind, but of filling it with Scripture. Read a verse slowly, write what you notice, and return to it at noon and at evening. Let the words of David, the shepherd and king, become your own words, and let the light of His presence steady your steps when the path grows narrow and the night seems long.</p>
        <p>The journal is arranged in four weeks: rest, trust, lament and praise. Each day opens with a Psalm, a short reflection, and space to record one blessing you would otherwise have missed. Use it alone at the kitchen table, with a spouse over coffee, or in a small group on Sunday evening. There is no right speed and no wrong answer. The goal is simply to meet God where He has promised to be found, in His Word, and to carry that meeting into the ordinary hours of work, family and waiting. May these mornings become a harvest you gather for many years.</p>
      </div>
      <p class="back-author">Elias&nbsp;&nbsp;Marrow</p>
    </section>

    <section class="spine">
      <div class="spine-art" role="img" aria-label="Edge of the heavenly cloud illustration in teal and gold"></div>
      <p class="spine-text">
        <span>Elias Marrow</span>
        <span class="spine-dot"></span>
        <span>Morning Harvest</span>
      </p>
    </section>

    <section class="front-cover">
      <div class="front-art" role="img" aria-label="Illustration of heavenly light breaking through golden and teal clouds"></div>
      <p class="series">Psalm Journal</p>
      <h1 class="front-title">MORNING<br>HARVEST</h1>
      <p class="front-subtitle">For the Weary Traveler<br>on the Narrow Road</p>
      <p class="front-author">Elias Marrow</p>
    </section>
  </main>
</body>
</html>
```